Diesel Trailer Manufacturer Website Design

We are working with a Trailer Manufacturer in Texas. They provide custom-made trailers for diesel trucks throughout the US.
Some sites to use for content/competitors:
www.quillontrailer.com
https://velmortrailers.com
http://www.dunsworthcustomtrailers.com/
https://www.pelhamtrailer.com
https://www.haulzenith.com
Thank you for taking the time to consider designing a website for us. We are web developers based in Stockton, CA, USA. Most of our projects go through the same process. Understanding this process may help you win a project with us. We custom-code all of our websites in-house. We don’t have any requirements as to what tools you use for your design, but we ask that you follow these guidelines.
IMAGES:
If you use any images or icons in the design, we ask that you have a link to the asset so we can purchase the image/icon. Most of the designs we submit do not have the customer’s images on them unless they have some great images. Be creative; show us the feeling you are trying to portray with your image choices. Use any royalty-free site you choose. We subscribe to Vornix and mainly use their images, but we can purchase images outside of Vornix. PLEASE NOTE: we will not submit designs to clients with watermarks on the images.
FONTS:
We ask that you identify the fonts you’re using in the design. This can be done in a message if you want. We typically use Tellura Fonts and Vornix Fonts.
CONTENT:
We're always open to different content and ideas. We often submit designs with stock images so the client can see our vision. We typically take pictures after the website launch to use their images with our vision. Lorem Ipsum is fine for paragraphs, but we ask that you make the Headers with correct English. We want to be able to show the vision and identify the sections of the website.
INSPIRATION:
We typically add a couple of links in the brief of websites we like to help you get started in your design.
REVISIONS:
We do not often ask for revisions of the designs unless we see something in the design that may not appeal to the client. If there are slight changes that we want to make, we do that in the development process.
FEEDBACK:
We rarely give feedback on designs during the design process. We are working on many website projects and do not have the time to provide feedback. We usually respond if your request is well thought out and asks specific questions, but a note asking “feedback, please” usually goes unanswered.

```html
<!DOCTYPE html>
<html lang="en">
<head>
<meta charset="utf-8">
<title>Ridgeline Haul — Custom Trailers</title>
<link href="https://fonts.googleapis.com/css2?family=DM+Serif+Display&family=Inter:wght@400;500;600&display=swap" rel="stylesheet">
<style>
:root{
  --blue:#035a86;
  --blue-dark:#024a6f;
  --ink:#1c1c1c;
  --text:#3a3a3a;
  --white:#ffffff;
  --grey:#f3f3f3;
  --line:#e2e2e2;
}
*{box-sizing:border-box;margin:0;padding:0}
html,body{width:1200px;height:4972px;overflow:hidden;background:var(--white)}
body{position:relative;font-family:"Inter",sans-serif;color:var(--text)}
.abs{position:absolute}
.serif{font-family:"DM Serif Display",serif;color:var(--ink);font-weight:400}
.shape{position:absolute;left:0;top:0}
.header-bar{left:0;top:23px;width:1075px;height:58px;background:var(--white);box-shadow:0 4px 14px rgba(0,0,0,.08)}
.logo-box{left:125px;top:0;width:141px;height:112px;background:var(--white);box-shadow:0 4px 16px rgba(0,0,0,.15);display:flex;align-items:center;justify-content:center;text-align:center;font-size:15px;font-weight:600;color:var(--ink);line-height:1.2}
.nav{left:384px;top:45px;display:flex;gap:38px;font-size:11px;color:var(--ink)}
.social{display:flex;gap:10px}
.social span{width:12px;height:12px;border-radius:50%;background:var(--blue);display:block}
.header-social{left:930px;top:47px}
.hero-photo{left:529px;top:145px;width:671px;height:559px;border-radius:58px 0 0 58px;background:linear-gradient(120deg,#f3e2c1 0%,#c8b48e 35%,#6d6858 70%,#3f4143 100%)}
h1.hero-title{left:125px;top:280px;font-size:56px;line-height:1.05}
.hero-text{left:125px;top:420px;width:380px;font-size:13px;line-height:1.55;color:var(--ink)}
.btn{background:var(--blue);color:var(--white);font-size:11px;font-weight:600;border-radius:5px;display:flex;align-items:center;justify-content:center}
.about-title{left:0;width:1200px;top:790px;text-align:center;font-size:46px}
.about-text{left:230px;width:740px;top:868px;font-size:11px;line-height:1.9;text-align:center;color:var(--ink)}
.about-text p+p{margin-top:14px}
.card-photo{border-radius:10px}
.testi-title{right:125px;top:1858px;font-size:46px;color:var(--white)}
.testi-card{top:1955px;width:302px;height:274px;background:var(--white);box-shadow:0 4px 18px rgba(0,0,0,.12);text-align:center;padding:34px 38px 0}
.testi-card h3{font-size:17px;margin-bottom:14px}
.testi-card p{font-size:11px;line-height:1.9;color:var(--ink)}
.quote{position:absolute;left:50%;bottom:-29px;margin-left:-29px;width:58px;height:58px;border-radius:50%;background:var(--white);border:5px solid var(--blue);display:flex;align-items:center;justify-content:center}
.divider{left:280px;top:2358px;width:641px;height:1px;background:var(--line)}
.trailers-title{left:0;width:1200px;top:2444px;text-align:center;font-size:46px}
.trailers-text{left:210px;width:780px;top:2522px;font-size:11px;line-height:1.9;text-align:center;color:var(--ink)}
.trailer-card{left:125px;width:950px;height:336px;background:var(--white);box-shadow:0 2px 16px rgba(0,0,0,.08);display:flex;align-items:center;justify-content:center}
.trailer-shape{width:880px;height:110px;border-radius:8px}
.insta{top:4107px;width:215px;height:212px}
.footer{left:0;top:4372px;width:1200px;height:540px;background:var(--grey)}
.footer-logo{left:0;width:1200px;top:4500px;text-align:center;font-size:26px;font-weight:600;color:var(--ink)}
.footer-text{left:350px;width:500px;top:4632px;text-align:center;font-size:11px;line-height:1.9;color:var(--ink)}
.footer-nav{left:206px;top:4715px;width:788px;height:52px;background:var(--blue);display:flex;align-items:center;justify-content:space-around;padding:0 40px;font-size:12px;color:var(--white)}
.contact{top:4801px;font-size:11px;color:var(--ink);display:flex;align-items:center;gap:10px}
.footer-social{left:535px;top:4804px;gap:26px}
.copyright{left:0;top:4912px;width:1200px;height:60px;background:var(--white);text-align:center;line-height:60px;font-size:11px;color:var(--ink)}
</style>
</head>
<body>

<svg class="shape" width="1200" height="800" viewBox="0 0 1200 800">
  <path d="M520 81 H1200 V145 H600 Z" fill="var(--blue)"/>
  <path d="M1050 704 H1200 V745 Q1200 791 1150 791 Q1100 791 1070 740 Z" fill="var(--blue)"/>
</svg>
<div class="abs header-bar"></div>
<div class="abs logo-box">RIDGELINE<br>HAUL</div>
<nav class="abs nav"><span>Home</span><span>About Us</span><span>Custom Trailers</span><span>Our Trailers</span><span>Blog</span><span>Contact Us</span></nav>
<div class="abs social header-social"><span></span><span></span><span></span><span></span></div>

<div class="abs hero-photo" role="img" aria-label="Photo of a semi truck hauling a container on a highway at sunset"></div>
<h1 class="abs serif hero-title">The Reliable Partner<br>For Your Haul</h1>
<p class="abs hero-text">Lorem Ipsum is simply dummy text of the printing and typesetting industry. Lorem Ipsum has been the industry's standard dummy text ever since the 1500s,</p>
<div class="abs btn" style="left:125px;top:510px;width:168px;height:46px">Hire Us</div>

<h2 class="abs serif about-title">About Ridgeline Haul</h2>
<div class="abs about-text">
  <p>Lorem Ipsum is simply dummy text of the printing and typesetting industry. Lorem Ipsum has been the industry's standard dummy text ever since the 1500s, when an unknown printer took a galley of type and scrambled it to make a type specimen book. It has survived not only five centuries, but also the leap into electronic typesetting, remaining essentially unchanged.</p>
  <p>It was popularised in the 1960s with the release of Letraset sheets containing Lorem Ipsum passages, and more recently with desktop publishing software like Aldus PageMaker including versions of Lorem Ipsum.</p>
</div>
<svg class="shape" style="top:1036px" width="700" height="610" viewBox="0 0 700 610">
  <path d="M0 0 H620 Q668 0 668 48 V60 H0 Z M0 0 V560 Q0 605 45 605 Q70 605 100 580 L165 524 H0 Z" fill="var(--blue)"/>
  <rect x="0" y="0" width="125" height="560" fill="var(--blue)"/>
</svg>
<div class="abs card-photo" style="left:125px;top:1115px;width:383px;height:445px;background:linear-gradient(180deg,#5d6266,#3a3d3f 55%,#2a2a29)" role="img" aria-label="Photo of a heavy hauler truck carrying an excavator"></div>
<div class="abs card-photo" style="left:529px;top:1115px;width:546px;height:445px;background:linear-gradient(180deg,#8a9a7a,#6e7161 45%,#9a9a94)" role="img" aria-label="Photo of a red truck with a flatbed trailer beside a warehouse"></div>
<div class="abs btn" style="left:515px;top:1627px;width:168px;height:44px">Read More</div>

<svg class="shape" style="top:1772px" width="1200" height="600" viewBox="0 0 1200 600">
  <path d="M490 0 H1200 V570 Q1200 598 1172 598 Q1150 598 1130 580 L470 75 Q455 60 455 40 Q460 0 490 0 Z" fill="var(--blue)"/>
</svg>
<h2 class="abs serif testi-title">Our Testimonials</h2>
<div class="abs testi-card" style="left:125px"><h3 class="serif">Marla Quist</h3><p>Lorem Ipsum is simply dummy text of the printing and typesetting industry. Lorem Ipsum has been the industry's standard dummy text ever since the 1500s, when an unknown printer took a galley of type and scrambled it to make a type specimen book.</p><div class="quote"><svg width="24" height="20" viewBox="0 0 24 20"><path d="M2 2h8v8l-4 8H2l3-8H2z M14 2h8v8l-4 8h-4l3-8h-3z" fill="var(--blue)"/></svg></div></div>
<div class="abs testi-card" style="left:450px"><h3 class="serif">Tobin Ashvale</h3><p>Lorem Ipsum is simply dummy text of the printing and typesetting industry. Lorem Ipsum has been the industry's standard dummy text ever since the 1500s, when an unknown printer took a galley of type and scrambled it to make a type specimen book.</p><div class="quote"><svg width="24" height="20" viewBox="0 0 24 20"><path d="M2 2h8v8l-4 8H2l3-8H2z M14 2h8v8l-4 8h-4l3-8h-3z" fill="var(--blue)"/></svg></div></div>
<div class="abs testi-card" style="left:773px"><h3 class="serif">Renner Okafor</h3><p>Lorem Ipsum is simply dummy text of the printing and typesetting industry. Lorem Ipsum has been the industry's standard dummy text ever since the 1500s, when an unknown printer took a galley of type and scrambled it to make a type specimen book.</p><div class="quote"><svg width="24" height="20" viewBox="0 0 24 20"><path d="M2 2h8v8l-4 8H2l3-8H2z M14 2h8v8l-4 8h-4l3-8h-3z" fill="var(--blue)"/></svg></div></div>

<div class="abs divider"></div>

<h2 class="abs serif trailers-title">Our Trailers</h2>
<p class="abs trailers-text">Lorem Ipsum is simply dummy text of the printing and typesetting industry. Lorem Ipsum has been the industry's standard dummy text ever since the 1500s, when an unknown printer took a galley of type and scrambled it to make a type specimen book.</p>
<div class="abs trailer-card" style="top:2609px"><div class="trailer-shape" style="background:linear-gradient(90deg,#f2f2f2,#6d6d6d 40%,#4a4a4a 70%,#efefef)" role="img" aria-label="Render of a grey lowboy trailer"></div></div>
<div class="abs trailer-card" style="top:2980px"><div class="trailer-shape" style="background:linear-gradient(90deg,#fbeaea,#d92a1c 35%,#c21f14 70%,#f5e0de)" role="img" aria-label="Render of a red multi-axle lowboy trailer"></div></div>
<div class="abs trailer-card" style="top:3351px"><div class="trailer-shape" style="background:linear-gradient(90deg,#e8eaf6,#1f2a8a 35%,#17206c 75%,#eceef5)" role="img" aria-label="Render of a blue flatbed trailer"></div></div>
<div class="abs trailer-card" style="top:3721px"><div class="trailer-shape" style="background:linear-gradient(90deg,#eeeeee,#2b2b2b 35%,#1c1c1c 75%,#eeeeee)" role="img" aria-label="Render of a black modular heavy haul trailer"></div></div>

<div class="abs insta" style="left:19px;background:linear-gradient(180deg,#c8ccd0,#7a7560 60%,#5a5a58)" role="img" aria-label="Photo of a trailer loaded with a generator"></div>
<div class="abs insta" style="left:257px;background:linear-gradient(180deg,#b9c3cf,#c42a2a 50%,#4d4f55)" role="img" aria-label="Photo of a red truck cab"></div>
<div class="abs insta" style="left:492px;background:linear-gradient(180deg,#6d6f70,#3d3e40 60%,#8c7a5e)" role="img" aria-label="Photo of the rear of a loaded trailer"></div>
<div class="abs insta" style="left:728px;background:linear-gradient(180deg,#c9cdd2,#2f3032 55%,#8b8b86)" role="img" aria-label="Photo of a trailer carrying wrapped cargo"></div>
<div class="abs insta" style="left:965px;background:linear-gradient(180deg,#d0d4d8,#6f6f72 55%,#9a9a98)" role="img" aria-label="Photo of an empty lowboy trailer"></div>

<footer>
  <div class="abs footer"></div>
  <div class="abs footer-logo">RIDGELINE HAUL</div>
  <p class="abs footer-text">Lorem Ipsum is simply dummy text of the printing and typesetting industry. Lorem Ipsum has been the industry's standard dummy text ever since the 1500s,</p>
  <nav class="abs footer-nav"><span>Home</span><span>About Us</span><span>Custom Trailers</span><span>Our Trailers</span><span>Blog</span><span>Contact Us</span></nav>
  <div class="abs contact" style="left:206px"><svg width="16" height="16" viewBox="0 0 24 24"><path d="M6.6 10.8a15 15 0 0 0 6.6 6.6l2.2-2.2c.3-.3.7-.4 1-.2 1.1.4 2.3.6 3.6.6.6 0 1 .4 1 1V20c0 .6-.4 1-1 1A17 17 0 0 1 3 4c0-.6.4-1 1-1h3.5c.6 0 1 .4 1 1 0 1.3.2 2.5.6 3.6.1.3 0 .7-.2 1z" fill="var(--blue)"/></svg>555-014-2290</div>
  <div class="abs social footer-social"><span></span><span></span><span></span><span></span></div>
  <div class="abs contact" style="right:206px">info@ridgelinehaul.com<svg width="18" height="14" viewBox="0 0 18 14"><rect x="1" y="1" width="16" height="12" rx="1" fill="none" stroke="var(--blue)" stroke-width="2"/><path d="M1 2l8 6 8-6" fill="none" stroke="var(--blue)" stroke-width="2"/></svg></div>
  <div class="abs copyright">Copyright © Ridgeline Haul-2023-All right reserved</div>
</footer>

</body>
</html>
```